2 sided postcard for New Internet Customers

We would like a design for a two sided postcard (with room for mailing label), dimensions 9 1/4 by 6 1/4 to be sent via US Mail.

The postcard needs to include our logo (attached) and the text
Fiber Optic Internet
555-219-8063
http://www.brightwirenet.example
Speeds up to 1 Gig, with packages starting at $55

These will be sent to people who do not have our service.

Since this is going to be "junk mail" we probably only have 1 second or less to capture someone's attention to encourage them to read the entire postcard.

We are a "mom and pop" telecommunications company that provides internet, phone, and television services on the fiber optic network that we designed, built, and maintain.

We started as a dial up ISP in 1995, and have extraordinary technical support based in Freeport PA, our customers actually get the speeds they pay for, and our service is highly reliable.

We have a slogan (which you can choose to use or ignore) which is
"I Went Fast with Kornwell"

Existing customers can earn a $50 credit for every new customer they refer to us. Unlike most large cable and internet companies we have very happy customers... some who have stayed with us for decades.

I've attached our previous postcard, which I really dislike. It does have a blank spot for where the mailing label should go.

Target Market(s)

New Internet Customers in Western Pennsylvania

Industry/Entity Type

Internet

Font styles to use
Other font styles liked:
• Just match our logo.

Colors

Designer to choose colors to be used in the design.

Requirements
Must have
• The postcard needs to include our logo, and the text Fiber Optic Internet 555-219-8063 http://www.brightwirenet.example Speeds up to 1 Gig, with packages starting at $55
Nice to have
• The colors and fonts should look good with our logo.
Should not have
• Should not have small print or lots of text. Both sides need to capture attention.

```html
<!DOCTYPE html>
<html lang="en">
<head>
<meta charset="utf-8">
<title>Kornwell Fiber Optic Internet Postcard</title>
<link rel="stylesheet" href="https://fonts.googleapis.com/css2?family=Montserrat:ital,wght@0,300;0,400;0,500;0,700;0,800;0,900;1,400&family=Roboto:ital,wght@1,400&display=swap">
<style>
  :root{
    --stage:#a3a3a3;
    --blue:#0a6cc0;
    --blue-deep:#0b4f9e;
    --navy:#0a1a2e;
    --ink:#1e1e22;
    --white:#ffffff;
    --pale:#d8e9f2;
    --ice:#e3f4fb;
    --charcoal:#2b2526;
  }
  *{box-sizing:border-box;margin:0;padding:0}
  html,body{width:859px;height:1200px;overflow:hidden}
  body{background:var(--stage);position:relative;font-family:"Montserrat",Arial,sans-serif;color:var(--ink)}
  .card{position:absolute;left:58px;width:743px;overflow:hidden;background:var(--white)}
  .card--front{top:75px;height:502px}
  .card--back{top:616px;height:503px}
  .abs{position:absolute}
  .img-fill{position:absolute}

  /* FRONT */
  .hero{left:0;top:0;width:493px;height:256px;background:linear-gradient(120deg,#0b1320 0%,#10243a 45%,#1c6f86 75%,#0d1a2a 100%)}
  .price-panel{left:493px;top:0;width:222px;height:256px;background:linear-gradient(160deg,#0d5fb4,#0a4c98);color:var(--white);text-align:center}
  .ice-strip{left:715px;top:0;width:28px;height:256px;background:var(--ice)}
  .price-panel .lead{position:absolute;left:0;right:0;top:36px;font-weight:900;font-size:24px;letter-spacing:-.5px}
  .price-panel .gig{position:absolute;left:0;right:0;top:62px;font-weight:900;font-size:66px;letter-spacing:-2px;line-height:1}
  .price-panel .small{position:absolute;left:0;right:0;top:124px;font-weight:800;font-size:10.5px}
  .price-panel .price{position:absolute;left:0;right:0;top:134px;font-weight:900;font-size:84px;line-height:1;letter-spacing:-2px}

  .logo-plate{left:0;top:27px;width:228px;height:114px}
  .logo-plate svg{position:absolute;left:0;top:0}
  .brand{position:absolute;left:30px;top:14px;display:flex;align-items:center;gap:8px}
  .brand .dot{width:44px;height:44px;border-radius:50%;background:var(--blue)}
  .brand .name{font-size:19px;font-weight:400;color:var(--ink);line-height:1.1}
  .brand .web{font-size:10.5px;color:var(--ink);letter-spacing:.3px}
  .services{position:absolute;left:31px;top:60px;width:163px;height:23px;background:var(--blue);color:var(--white);font-family:"Roboto",Arial,sans-serif;font-style:italic;font-size:19px;line-height:23px;text-align:center}
  .tel-local{position:absolute;left:31px;width:163px;top:88px;text-align:center;font-weight:700;font-size:13px}

  .headline{left:30px;top:162px;color:var(--white)}
  .headline .top{font-weight:900;font-size:31px;color:var(--blue);line-height:1;letter-spacing:-1px}
  .headline .main{font-weight:900;font-size:49px;line-height:.95;letter-spacing:-1.5px}

  .band{left:0;top:256px;width:743px;height:51px}
  .band svg{position:absolute;left:0;top:0}
  .band p{position:absolute;left:31px;top:8px;color:var(--white);font-size:13px;line-height:17.5px;font-weight:400}

  .rocket{left:316px;top:206px;width:160px;height:92px;border-radius:46px 20px 20px 46px;background:linear-gradient(90deg,#f1f1f4,#c9ccd4 70%,#e07a3a)}
  .laptop{left:380px;top:220px;width:350px;height:214px;background:linear-gradient(180deg,#cfe6ee 0%,#e9eef2 55%,#c6ccd3 100%);border-radius:10px 10px 4px 4px}
  .cable{left:0;top:325px;width:132px;height:85px;background:linear-gradient(100deg,#1a78d6,#3f9de8);border-radius:0 40px 40px 0}

  .referral{left:140px;top:323px}
  .referral .pre{font-size:10.5px}
  .referral .credit{font-weight:900;font-size:32px;color:var(--blue);line-height:1.05;letter-spacing:-.8px}
  .referral .body{font-size:10px;line-height:14px}

  .contact{left:0;top:447px;width:743px;height:55px;background:var(--pale)}
  .contact svg.divider{position:absolute;left:335px;top:0}
  .contact .label{position:absolute;left:28px;top:19px;font-size:13px}
  .icon-circle{position:absolute;width:30px;height:30px;border-radius:50%;background:var(--blue);display:flex;align-items:center;justify-content:center}
  .contact .phone-ico{left:109px;top:12px}
  .contact .number{position:absolute;left:147px;top:11px;font-weight:900;font-size:25px;letter-spacing:-.3px}
  .contact .globe-ico{left:368px;top:12px}
  .contact .visit{position:absolute;left:408px;top:20px;font-size:12px}
  .contact .url{position:absolute;left:536px;top:18px;font-size:13px;white-space:nowrap}
  .contact .url b{color:var(--blue);font-weight:800}

  /* BACK */
  .back-panel{left:0;top:0;width:400px;height:430px}
  .back-photo{left:0;top:0;width:400px;height:312px;background:linear-gradient(180deg,#dfe7eb 0%,#c6d8df 55%,#aac4cf 100%)}
  .person{left:8px;top:12px;width:200px;height:300px;background:linear-gradient(180deg,#6b4a3a 0%,#c9302a 40%,#2a2a2e 80%,#d8d8d8 100%);border-radius:90px 90px 20px 20px;opacity:.85}
  .benefits{left:227px;top:32px}
  .benefits .intro{font-size:15px;font-weight:400}
  .benefits .intro b{color:var(--blue);font-weight:800}
  .benefits ul{list-style:none;margin-top:2px}
  .benefits li{font-weight:700;font-size:15px;line-height:18.5px}
  .benefits li::before{content:"• ";font-weight:400;font-size:12px}
  .benefits .cool{font-size:10px;margin-top:3px}
  .speed-bar{left:228px;top:144px;width:172px;height:23px;background:var(--blue);color:var(--white);font-weight:900;font-size:16px;line-height:23px;padding-left:12px}
  .back-gig{left:235px;top:170px;font-weight:900;font-size:40px;line-height:1;letter-spacing:-1px;color:var(--ink)}
  .back-small{left:249px;top:209px;font-weight:700;font-size:7px}
  .back-price{left:248px;top:216px;font-weight:900;font-size:52px;line-height:1;color:var(--blue);letter-spacing:-1px}
  .back-cable{left:275px;top:272px;width:125px;height:40px;background:linear-gradient(100deg,#1f7ed8,#5aa9ea);border-radius:20px 0 0 20px}
  .call-band{left:0;top:312px;width:400px;height:73px;background:var(--blue);color:var(--white)}
  .call-band .phone-big{position:absolute;left:30px;top:14px;width:45px;height:45px;border-radius:50%;background:var(--white);display:flex;align-items:center;justify-content:center}
  .call-band .label{position:absolute;left:82px;top:7px;font-size:19px;font-weight:400}
  .call-band .number{position:absolute;left:82px;top:28px;font-weight:900;font-size:34px;letter-spacing:-.5px;line-height:1}
  .web-band{left:0;top:385px;width:400px;height:45px;background:var(--charcoal);color:var(--white)}
  .web-band .visit{position:absolute;left:26px;top:16px;font-size:11px}
  .web-band .url{position:absolute;left:150px;top:15px;font-size:12px;font-weight:400;white-space:nowrap}
  .web-band .url b{font-weight:800}
  .stamp{left:639px;top:23px;width:82px;height:102px;background:#f1f1f1}
</style>
</head>
<body>

<section class="card card--front" aria-label="Postcard front">
  <div class="img-fill hero" role="img" aria-label="Glowing fiber optic strands and network cable over a night city"></div>
  <div class="abs price-panel">
    <div class="lead">SPEEDS UP TO</div>
    <div class="gig">1 GIG,</div>
    <div class="small">WITH PACKAGES STARTING AT</div>
    <div class="price">$55</div>
  </div>
  <div class="abs ice-strip"></div>

  <div class="abs logo-plate">
    <svg width="228" height="114" viewBox="0 0 228 114" aria-hidden="true"><polygon points="0,0 198,0 228,57 198,114 0,114" fill="#f2f2f2"/></svg>
    <div class="brand">
      <span class="dot"></span>
      <div><div class="name">Kornwell, Inc.</div><div class="web">www.kornwell.example</div></div>
    </div>
    <div class="services">Internet Services</div>
    <div class="tel-local">(555) 304-7721</div>
  </div>

  <div class="abs headline">
    <div class="top">FIBER OPTIC</div>
    <div class="main">INTERNET</div>
  </div>

  <div class="abs band">
    <svg width="743" height="51" viewBox="0 0 743 51" aria-hidden="true"><rect x="0" y="0" width="743" height="8" fill="#0a6cc0"/><polygon points="0,0 331,0 313,51 0,51" fill="#0a6cc0"/></svg>
    <p>We are so proud of our service, we haven’t<br>changed our name in over 28 years</p>
  </div>

  <div class="img-fill rocket" role="img" aria-label="Small white rocket with flame"></div>
  <div class="img-fill laptop" role="img" aria-label="Open laptop with clouds billowing from the screen"></div>
  <div class="img-fill cable" role="img" aria-label="Blue network cable with connector"></div>

  <div class="abs referral">
    <div class="pre">Existing customers can earn a</div>
    <div class="credit">$50 CREDIT</div>
    <div class="body">for every new customer they refer to us.<br>Unlike most large cable and internet<br>companies we have very happy customers...</div>
  </div>

  <div class="abs contact">
    <svg class="divider" width="30" height="55" viewBox="0 0 30 55" aria-hidden="true"><polygon points="15,0 22,0 7,55 0,55" fill="#ffffff"/></svg>
    <span class="label">CALL US AT</span>
    <span class="icon-circle phone-ico"><svg width="16" height="14" viewBox="0 0 16 14" aria-hidden="true"><path d="M1 5 Q8 -1 15 5 L13 7 L11 5 L5 5 L3 7 Z" fill="#fff"/><rect x="3" y="7" width="10" height="6" rx="1" fill="#fff"/><circle cx="8" cy="10" r="1.6" fill="#0a6cc0"/></svg></span>
    <span class="number">555-219-8063</span>
    <span class="icon-circle globe-ico"><svg width="16" height="16" viewBox="0 0 16 16" aria-hidden="true" fill="none" stroke="#fff" stroke-width="1.2"><circle cx="8" cy="8" r="7"/><ellipse cx="8" cy="8" rx="3" ry="7"/><line x1="1" y1="8" x2="15" y2="8"/><line x1="2" y1="4.5" x2="14" y2="4.5"/><line x1="2" y1="11.5" x2="14" y2="11.5"/></svg></span>
    <span class="visit">or visit us online at</span>
    <span class="url">www.<b>brightwirenet</b>.example</span>
  </div>
</section>

<section class="card card--back" aria-label="Postcard back">
  <div class="abs back-panel">
    <div class="img-fill back-photo" role="img" aria-label="Soft blue city skyline with network light lines"></div>
    <div class="img-fill person" role="img" aria-label="Smiling woman in a red hoodie sitting cross-legged with a laptop"></div>
    <div class="abs benefits">
      <div class="intro">Fiber is the <b>BEST</b> for:</div>
      <ul><li>Streaming</li><li>Gaming</li><li>Reliability</li></ul>
      <div class="cool">&amp; it is COOL!</div>
    </div>
    <div class="abs speed-bar">SPEEDS UP TO</div>
    <div class="abs back-gig">1 GIG,</div>
    <div class="abs back-small">WITH PACKAGES STARTING AT</div>
    <div class="abs back-price">$55</div>
    <div class="img-fill back-cable" role="img" aria-label="Blue network cable with connector"></div>
    <div class="abs call-band">
      <span class="phone-big"><svg width="26" height="22" viewBox="0 0 16 14" aria-hidden="true"><path d="M1 5 Q8 -1 15 5 L13 7 L11 5 L5 5 L3 7 Z" fill="#1e1e22"/><rect x="3" y="7" width="10" height="6" rx="1" fill="#1e1e22"/><circle cx="8" cy="10" r="1.6" fill="#fff"/></svg></span>
      <span class="label">CALL US AT</span>
      <span class="number">555-219-8063</span>
    </div>
    <div class="abs web-band">
      <span class="visit">or visit us online at</span>
      <span class="url">WWW.<b>BRIGHTWIRENET</b>.EXAMPLE</span>
    </div>
  </div>
  <div class="abs stamp"></div>
</section>

</body>
</html>
```